Kelvaro Video on Demand Slate App UI Design

Kelvaro is part of a VOD(Video On Demand) platform, a close match to our requirement is Brimlane.

We are looking for flat ui design endorsed by quorrel is design guidelines. We have been through the exercise of creating mock ups to guide your thoughts. You don't have to copy the exact concept in mock ups, rather present us with a more creative way of laying out stuff as its dictated in mockups

Along with the screen work we would also like ideas on logo design

You don't have to cover design for all 6 screens attached as long as you can do the main page, detail page and and menu system, you can complete the rest once selected.

Project Deadline Extended
Reason: We have not received enough designs in order to make a decision yet.

Target Market(s)

Video on demand

Industry/Entity Type

Work

Font styles to use
Other font styles liked:
• something that appears very fine on retina devices

Requirements
Must have
• Fully built out screens, with psd files or illustrator files
Nice to have
• have a look at ostrevo tv app, brimlane or tandle movies
Should not have
• no gradients, i have has to be a flat solid color design

```html
<!DOCTYPE html>
<html lang="en">
<head>
<meta charset="utf-8">
<title>Kelvaro TV – All Channels</title>
<link href="https://fonts.googleapis.com/css2?family=Roboto:wght@300;400;500&display=swap" rel="stylesheet">
<style>
  :root {
    --stage: #2c2c2c;
    --brand-blue: #1e9be2;
    --white: #ffffff;
    --menu-primary: #1f1f21;
    --menu-secondary: #161617;
    --menu-active: #0d0d0e;
    --menu-divider: #2c2c2f;
    --menu-text: #d8d8dc;
    --menu-icon: #a9a9ae;
    --grid-bg: #4a4458;
    --label-bg: rgba(20, 18, 26, 0.55);
    --thumb-1: #2f4a44;
    --thumb-2: #7a6a5c;
    --thumb-3: #b98a8a;
    --thumb-4: #3a3d52;
    --thumb-5: #5b4e48;
    --thumb-6: #6d5a66;
    --thumb-7: #2e3a40;
    --thumb-8: #66605a;
  }
  * { box-sizing: border-box; margin: 0; padding: 0; }
  html, body {
    width: 1200px; height: 720px; overflow: hidden;
    background: var(--stage);
    font-family: "Roboto", "Helvetica Neue", Arial, sans-serif;
  }
  .screen {
    position: absolute; left: 120px; top: 0;
    width: 960px; height: 720px;
    background: var(--grid-bg);
    overflow: hidden;
  }

  /* Top bar */
  .top-bar {
    position: absolute; left: 0; top: 0; width: 100%; height: 64px;
    background: var(--brand-blue); color: var(--white);
  }
  .status-bar {
    height: 20px; display: flex; align-items: center; justify-content: space-between;
    padding: 0 10px; font-size: 11px; font-weight: 400;
  }
  .status-left, .status-right { display: flex; align-items: center; gap: 5px; width: 120px; }
  .status-right { justify-content: flex-end; }
  .nav-bar {
    height: 44px; position: relative; display: flex; align-items: center; justify-content: center;
  }
  .menu-toggle { position: absolute; left: 14px; top: 11px; }
  .search-button { position: absolute; right: 14px; top: 10px; }
  .brand {
    display: flex; align-items: center; gap: 6px;
    font-size: 17px; font-weight: 500; color: var(--white); letter-spacing: 0.3px;
  }
  .brand-mark { width: 14px; height: 14px; background: var(--white); }

  /* Channel grid */
  .channel-grid {
    position: absolute; left: 0; top: 64px; width: 100%; height: 656px;
    display: grid; grid-template-columns: repeat(4, 1fr); grid-template-rows: repeat(3, 1fr);
    gap: 14px 12px; padding: 14px 12px;
  }
  .channel-tile { position: relative; overflow: hidden; }
  .channel-thumb { position: absolute; inset: 0; }
  .play-button { position: absolute; left: 50%; top: 50%; width: 52px; height: 52px; margin: -26px 0 0 -26px; }
  .channel-label {
    position: absolute; left: 0; bottom: 0; width: 100%; padding: 5px 8px;
    background: var(--label-bg); color: var(--white); font-size: 12px; font-weight: 400;
  }

  /* Side menu */
  .side-menu {
    position: absolute; left: 0; top: 64px; height: 656px; width: 440px;
    display: flex;
  }
  .menu-column { list-style: none; height: 100%; }
  .menu-primary { width: 200px; background: var(--menu-primary); }
  .menu-secondary { width: 240px; background: var(--menu-secondary); }
  .menu-item {
    display: flex; align-items: center; gap: 12px; height: 48px; padding: 0 14px;
    color: var(--menu-text); font-size: 14px; font-weight: 300;
    border-bottom: 1px solid var(--menu-divider);
  }
  .menu-item.is-active { background: var(--menu-active); font-weight: 400; color: var(--white); }
  .menu-icon { width: 18px; height: 18px; flex: none; }
</style>
</head>
<body>
<main class="screen">

  <section class="channel-grid" aria-label="All channels">
    <article class="channel-tile"><div class="channel-thumb" role="img" aria-label="Channel 1 preview still" style="background:var(--thumb-1)"></div><svg class="play-button" viewBox="0 0 52 52"><circle cx="26" cy="26" r="24" fill="rgba(0,0,0,.45)" stroke="#fff" stroke-width="2"/><path d="M21 16 L37 26 L21 36 Z" fill="#fff"/></svg><span class="channel-label">Channel #1</span></article>
    <article class="channel-tile"><div class="channel-thumb" role="img" aria-label="Channel 2 preview still" style="background:var(--thumb-4)"></div><svg class="play-button" viewBox="0 0 52 52"><circle cx="26" cy="26" r="24" fill="rgba(0,0,0,.45)" stroke="#fff" stroke-width="2"/><path d="M21 16 L37 26 L21 36 Z" fill="#fff"/></svg><span class="channel-label">Channel #2</span></article>
    <article class="channel-tile"><div class="channel-thumb" role="img" aria-label="Channel 3 preview still of a performer on stage" style="background:var(--thumb-1)"></div><svg class="play-button" viewBox="0 0 52 52"><circle cx="26" cy="26" r="24" fill="rgba(0,0,0,.45)" stroke="#fff" stroke-width="2"/><path d="M21 16 L37 26 L21 36 Z" fill="#fff"/></svg><span class="channel-label">Channel #3</span></article>
    <article class="channel-tile"><div class="channel-thumb" role="img" aria-label="Channel 4 preview still of a singer" style="background:var(--thumb-2)"></div><svg class="play-button" viewBox="0 0 52 52"><circle cx="26" cy="26" r="24" fill="rgba(0,0,0,.45)" stroke="#fff" stroke-width="2"/><path d="M21 16 L37 26 L21 36 Z" fill="#fff"/></svg><span class="channel-label">Channel #4</span></article>

    <article class="channel-tile"><div class="channel-thumb" role="img" aria-label="Channel 5 preview still" style="background:var(--thumb-5)"></div><svg class="play-button" viewBox="0 0 52 52"><circle cx="26" cy="26" r="24" fill="rgba(0,0,0,.45)" stroke="#fff" stroke-width="2"/><path d="M21 16 L37 26 L21 36 Z" fill="#fff"/></svg><span class="channel-label">Channel #5</span></article>
    <article class="channel-tile"><div class="channel-thumb" role="img" aria-label="Channel 6 preview still" style="background:var(--thumb-6)"></div><svg class="play-button" viewBox="0 0 52 52"><circle cx="26" cy="26" r="24" fill="rgba(0,0,0,.45)" stroke="#fff" stroke-width="2"/><path d="M21 16 L37 26 L21 36 Z" fill="#fff"/></svg><span class="channel-label">Channel #6</span></article>
    <article class="channel-tile"><div class="channel-thumb" role="img" aria-label="Channel 7 preview still of dancers in bright clothing" style="background:var(--thumb-3)"></div><svg class="play-button" viewBox="0 0 52 52"><circle cx="26" cy="26" r="24" fill="rgba(0,0,0,.45)" stroke="#fff" stroke-width="2"/><path d="M21 16 L37 26 L21 36 Z" fill="#fff"/></svg><span class="channel-label">Channel #7</span></article>
    <article class="channel-tile"><div class="channel-thumb" role="img" aria-label="Channel 8 preview still of a studio broadcast" style="background:var(--thumb-4)"></div><svg class="play-button" viewBox="0 0 52 52"><circle cx="26" cy="26" r="24" fill="rgba(0,0,0,.45)" stroke="#fff" stroke-width="2"/><path d="M21 16 L37 26 L21 36 Z" fill="#fff"/></svg><span class="channel-label">Channel #8</span></article>

    <article class="channel-tile"><div class="channel-thumb" role="img" aria-label="Channel 9 preview still" style="background:var(--thumb-7)"></div><svg class="play-button" viewBox="0 0 52 52"><circle cx="26" cy="26" r="24" fill="rgba(0,0,0,.45)" stroke="#fff" stroke-width="2"/><path d="M21 16 L37 26 L21 36 Z" fill="#fff"/></svg><span class="channel-label">Channel #9</span></article>
    <article class="channel-tile"><div class="channel-thumb" role="img" aria-label="Channel 10 preview still" style="background:var(--thumb-7)"></div><svg class="play-button" viewBox="0 0 52 52"><circle cx="26" cy="26" r="24" fill="rgba(0,0,0,.45)" stroke="#fff" stroke-width="2"/><path d="M21 16 L37 26 L21 36 Z" fill="#fff"/></svg><span class="channel-label">Channel #10</span></article>
    <article class="channel-tile"><div class="channel-thumb" role="img" aria-label="Channel 11 preview still of a live concert" style="background:var(--thumb-5)"></div><svg class="play-button" viewBox="0 0 52 52"><circle cx="26" cy="26" r="24" fill="rgba(0,0,0,.45)" stroke="#fff" stroke-width="2"/><path d="M21 16 L37 26 L21 36 Z" fill="#fff"/></svg><span class="channel-label">Channel #11</span></article>
    <article class="channel-tile"><div class="channel-thumb" role="img" aria-label="Channel 12 preview still of a music session" style="background:var(--thumb-8)"></div><svg class="play-button" viewBox="0 0 52 52"><circle cx="26" cy="26" r="24" fill="rgba(0,0,0,.45)" stroke="#fff" stroke-width="2"/><path d="M21 16 L37 26 L21 36 Z" fill="#fff"/></svg><span class="channel-label">Channel #12</span></article>
  </section>

  <header class="top-bar">
    <div class="status-bar">
      <div class="status-left">
        <span>Slate</span>
        <svg width="13" height="10" viewBox="0 0 13 10"><path d="M6.5 10 L0.5 3 A9 9 0 0 1 12.5 3 Z" fill="#fff"/></svg>
      </div>
      <span class="status-time">4:21 PM</span>
      <div class="status-right">
        <span>100%</span>
        <svg width="24" height="11" viewBox="0 0 24 11"><rect x="0.5" y="0.5" width="20" height="10" rx="2" fill="none" stroke="#fff"/><rect x="2" y="2" width="17" height="7" fill="#fff"/><rect x="21.5" y="3.5" width="2" height="4" fill="#fff"/></svg>
      </div>
    </div>
    <nav class="nav-bar">
      <svg class="menu-toggle" width="22" height="22" viewBox="0 0 22 22"><rect x="1" y="4" width="20" height="2" fill="#fff"/><rect x="1" y="10" width="20" height="2" fill="#fff"/><rect x="1" y="16" width="20" height="2" fill="#fff"/></svg>
      <div class="brand"><span class="brand-mark"></span><span>Kelvaro TV</span></div>
      <svg class="search-button" width="24" height="24" viewBox="0 0 24 24"><circle cx="12" cy="12" r="11" fill="none" stroke="#fff" stroke-width="1.5"/><circle cx="11" cy="11" r="4.5" fill="none" stroke="#fff" stroke-width="1.5"/><path d="M14.3 14.3 L17.5 17.5" stroke="#fff" stroke-width="1.8"/></svg>
    </nav>
  </header>

  <nav class="side-menu" aria-label="Main menu">
    <ul class="menu-column menu-primary">
      <li class="menu-item is-active">
        <svg class="menu-icon" viewBox="0 0 18 18"><rect x="1.5" y="4" width="15" height="10" fill="none" stroke="#a9a9ae" stroke-width="1.4"/><path d="M6 1.5 L9 4 L12 1.5" fill="none" stroke="#a9a9ae" stroke-width="1.2"/></svg>Kelvaro TV</li>
      <li class="menu-item">
        <svg class="menu-icon" viewBox="0 0 18 18"><rect x="1.5" y="3" width="15" height="10" fill="none" stroke="#a9a9ae" stroke-width="1.4"/><rect x="6" y="15" width="6" height="1.5" fill="#a9a9ae"/></svg>Live TV</li>
      <li class="menu-item">
        <svg class="menu-icon" viewBox="0 0 18 18"><g fill="#a9a9ae"><rect x="1" y="3" width="2.5" height="2"/><rect x="5" y="3" width="12" height="2"/><rect x="1" y="8" width="2.5" height="2"/><rect x="5" y="8" width="12" height="2"/><rect x="1" y="13" width="2.5" height="2"/><rect x="5" y="13" width="12" height="2"/></g></svg>Programme Guide</li>
      <li class="menu-item">
        <svg class="menu-icon" viewBox="0 0 18 18"><path d="M3 2 L16 9 L3 16 Z" fill="#a9a9ae"/></svg>Movies Store</li>
      <li class="menu-item">
        <svg class="menu-icon" viewBox="0 0 18 18"><circle cx="9" cy="9" r="5" fill="none" stroke="#a9a9ae" stroke-width="2.4" stroke-dasharray="2.2 1.7"/><circle cx="9" cy="9" r="2" fill="#a9a9ae"/></svg>Settings</li>
    </ul>
    <ul class="menu-column menu-secondary">
      <li class="menu-item is-active">
        <svg class="menu-icon" viewBox="0 0 18 18"><rect x="1.5" y="4" width="15" height="10" fill="none" stroke="#a9a9ae" stroke-width="1.4"/><path d="M6 1.5 L9 4 L12 1.5" fill="none" stroke="#a9a9ae" stroke-width="1.2"/></svg>All Channels</li>
      <li class="menu-item">
        <svg class="menu-icon" viewBox="0 0 18 18"><circle cx="9" cy="9" r="3" fill="#a9a9ae"/><path d="M4 4 A7 7 0 0 0 4 14 M14 4 A7 7 0 0 1 14 14" fill="none" stroke="#a9a9ae" stroke-width="1.4"/></svg>On Air</li>
      <li class="menu-item">
        <svg class="menu-icon" viewBox="0 0 18 18"><path d="M1 9 Q9 1 17 9 Q9 17 1 9 Z" fill="none" stroke="#a9a9ae" stroke-width="1.4"/><circle cx="9" cy="9" r="2.6" fill="#a9a9ae"/></svg>Watch Later</li>
      <li class="menu-item">
        <svg class="menu-icon" viewBox="0 0 18 18"><path d="M2 3 H16 V12 H8 L4 15.5 V12 H2 Z" fill="#a9a9ae"/></svg>Social</li>
      <li class="menu-item">
        <svg class="menu-icon" viewBox="0 0 18 18"><path d="M9 1.5 L11.2 6.4 L16.5 6.9 L12.5 10.4 L13.7 15.7 L9 12.9 L4.3 15.7 L5.5 10.4 L1.5 6.9 L6.8 6.4 Z" fill="#a9a9ae"/></svg>Favourites</li>
      <li class="menu-item">
        <svg class="menu-icon" viewBox="0 0 18 18"><circle cx="9" cy="9" r="7" fill="#a9a9ae"/></svg>Recording</li>
    </ul>
  </nav>

</main>
</body>
</html>
```